Styling of small website for mid-sized Engineering and Manufacturing company

We need the styling for a professional website for a company wich delivers: engineering, manufacturing, assembling, servicing and prototyping. (typically, they produce complex devices in limited series (1-100 pieces. The client comes with an idea and they translate it into design and device).
We have already made a wire-frame, but need a style (colors, fonts, H1, H2, paragraphs, margins, padding etc).
The style must :
- express profession attitude (world of engineering)
- have a fresh, modern look
- be sober (enough (white) space between the elements
The style must also be able to be used in a RWD. At this moment the logo (just letters) uses a green color (#4C6E33), but it isn't an obligation to use the exact same color (even not the 'green' color itself if you think another color is better for the site).
engineering and production
It Company
Coded - Design and coding required
5+ page

```html
<!DOCTYPE html>
<html lang="en">
<head>
<meta charset="utf-8">
<title>Forgewell – Engineering &amp; Manufacturing</title>
<link rel="stylesheet" href="https://fonts.googleapis.com/css2?family=Roboto:wght@300;400;500&display=swap">
<style>
  :root {
    --brand-blue: #123e84;
    --brand-blue-dark: #0e3577;
    --text-dark: #222222;
    --text-body: #555555;
    --bg-white: #ffffff;
    --bg-soft: #fafafa;
    --bg-header: #fbfbfb;
    --bg-placeholder: #f1f1f1;
    --footer-bg: #2a2a2a;
    --footer-line: #3a3a3a;
    --footer-text: #ffffff;
    --button-bg: #1a1a1a;
  }
  * { box-sizing: border-box; margin: 0; padding: 0; }
  html, body { width: 880px; height: 1200px; overflow: hidden; }
  body { font-family: "Roboto", Arial, sans-serif; color: var(--text-dark); background: var(--bg-white); }
  .page { position: relative; width: 880px; height: 1200px; }

  .site-header { height: 62px; background: var(--bg-header); position: relative; }
  .site-logo { position: absolute; left: 138px; top: 10px; font-size: 38px; font-weight: 300; letter-spacing: 1px; color: var(--text-dark); }
  .main-nav { position: absolute; left: 402px; top: 0; height: 62px; display: flex; list-style: none; }
  .main-nav li { height: 62px; display: flex; align-items: center; padding: 0 11px; font-size: 8.6px; text-transform: uppercase; color: var(--text-dark); }
  .main-nav li.is-active { background: var(--brand-blue); color: #fff; }

  .hero { height: 324px; position: relative; display: flex; align-items: center; justify-content: center;
    background: linear-gradient(120deg, #2c4a78 0%, #7d95b8 30%, #a9bbd3 48%, #3e5a85 70%, #18263d 100%); }
  .hero-title { color: #fff; font-weight: 400; font-size: 29px; margin-top: -38px; }

  .intro { height: 152px; text-align: center; padding-top: 34px; }
  .section-title-blue { color: var(--brand-blue); font-weight: 400; font-size: 19.5px; }
  .intro p { width: 585px; margin: 14px auto 0; font-size: 10px; line-height: 16.5px; color: var(--text-body); }

  .works { height: 265px; background: var(--bg-soft); padding-top: 32px; }
  .works-title { text-align: center; font-weight: 400; font-size: 22px; color: var(--text-dark); }
  .work-grid { display: flex; gap: 17px; margin: 20px 0 0 140px; }
  .work-card { width: 137px; }
  .work-photo { height: 109px; }
  .work-label { height: 41px; background: var(--brand-blue-dark); color: #fff; font-size: 11.5px; font-weight: 500;
    display: flex; align-items: center; justify-content: center; text-transform: uppercase; letter-spacing: .3px; }

  .showcase { height: 235px; position: relative; }
  .sub-title { color: var(--brand-blue); font-weight: 500; font-size: 11.5px; text-transform: uppercase; line-height: 16.5px; }
  .showcase-main { position: absolute; left: 140px; top: 48px; }
  .client-box { position: absolute; left: 0; top: 28px; width: 164px; height: 125px; background: var(--bg-placeholder);
    display: flex; align-items: center; justify-content: center; color: var(--text-body); font-weight: 400; font-size: 18px; }
  .showcase-text { position: absolute; left: 181px; top: 27px; width: 240px; font-size: 10px; line-height: 16.5px; color: var(--text-body); }
  .reasons { position: absolute; left: 590px; top: 48px; width: 160px; }
  .reasons ul { list-style: none; margin-top: 8px; }
  .reasons li { display: flex; align-items: center; gap: 8px; height: 20px; font-size: 10px; color: var(--text-body); }
  .reasons svg { flex: none; }

  .site-footer { position: absolute; left: 0; top: 1038px; width: 880px; height: 162px; background: var(--footer-bg); color: var(--footer-text); }
  .footer-col { position: absolute; top: 29px; font-size: 9.2px; line-height: 15px; }
  .footer-col h3 { font-size: 11.5px; font-weight: 400; text-transform: uppercase; margin-bottom: 9px; }
  .map-button { display: inline-flex; align-items: center; gap: 6px; margin-top: 8px; height: 20px; padding: 0 8px;
    background: var(--button-bg); font-size: 8.5px; color: #fff; }
  .footer-bottom { position: absolute; left: 0; top: 123px; width: 880px; height: 39px; border-top: 1px solid var(--footer-line);
    display: flex; align-items: center; justify-content: center; font-size: 8.5px; }
</style>
</head>
<body>
<div class="page">
  <header class="site-header">
    <div class="site-logo">LOGO</div>
    <ul class="main-nav">
      <li class="is-active">Home</li>
      <li>Services</li>
      <li>Portfolio</li>
      <li>News</li>
      <li>About Forgewell</li>
      <li>Contact</li>
    </ul>
  </header>

  <section class="hero" role="img" aria-label="Close-up photo of large steel gear wheels in blue tones">
    <h1 class="hero-title">ENGINEERING &amp; MANUFACTURING</h1>
  </section>

  <section class="intro">
    <h2 class="section-title-blue">TECHNOLOGICAL SOLUTION IDEA TO PRODUCT</h2>
    <p>Forgewell ontwerpt en fabriceert te estellen voor de meest uniteenlopende industrieen. Met als belangrijkste de (para) medische sector. Onze Oplossingen zijn even veelzildig als de vragen van onze klanten. Engineering, prototype, (serie) productie en service onder een dak. Dat maakt het traject van vraag naar opplossing sneller en beter beheersbaar.</p>
  </section>

  <section class="works">
    <h2 class="works-title">OUR WORKS</h2>
    <div class="work-grid">
      <div class="work-card">
        <div class="work-photo" role="img" aria-label="Engineers reviewing plans in a workshop" style="background:linear-gradient(160deg,#c9cfc8,#6f7a6c 60%,#3f4a3c)"></div>
        <div class="work-label">Engineering</div>
      </div>
      <div class="work-card">
        <div class="work-photo" role="img" aria-label="Metal part being turned on a lathe" style="background:linear-gradient(150deg,#2c5d83,#9fb0bd 50%,#5e6b74)"></div>
        <div class="work-label">Prototyping</div>
      </div>
      <div class="work-card">
        <div class="work-photo" role="img" aria-label="Technician assembling machinery" style="background:linear-gradient(160deg,#4d6a3a,#7c7a5e 50%,#3a3e44)"></div>
        <div class="work-label">Assembleren</div>
      </div>
      <div class="work-card">
        <div class="work-photo" role="img" aria-label="Welder at work with sparks" style="background:linear-gradient(160deg,#2f4f86,#6a7897 50%,#b8c2d8)"></div>
        <div class="work-label">Servicing</div>
      </div>
    </div>
  </section>

  <section class="showcase">
    <div class="showcase-main">
      <h3 class="sub-title">Showcase client X</h3>
      <div class="client-box">Aeronova</div>
      <p class="showcase-text">Lorem ipsum dolor sit amet, consectetur adipiscing elit. Nulla quam velit, vulputate eu pharetra nec, mattis ac neque. Duis vulputate commodo lectus, ac blandit elit tincidunt id. Sed rhoncus, tortor sed eleifend tristique, tortor mauris molestie elit, et lacinia ipsum quam nec dui. Quisque nec mauric sit amet elit iaculis pretium sit amet quis magna. Aenean velit odio, elementum in tempus ut, vehicula eu diam.</p>
    </div>
    <div class="reasons">
      <h3 class="sub-title">Waarom klanten voor ons kiezen</h3>
      <ul>
        <li><svg width="9" height="9" viewBox="0 0 10 10"><circle cx="5" cy="5" r="5" fill="#123e84"/><path d="M2.8 5.1l1.5 1.5 2.9-3" stroke="#fff" stroke-width="1.3" fill="none"/></svg>Al 4.251 abonnees</li>
        <li><svg width="9" height="9" viewBox="0 0 10 10"><circle cx="5" cy="5" r="5" fill="#123e84"/><path d="M2.8 5.1l1.5 1.5 2.9-3" stroke="#fff" stroke-width="1.3" fill="none"/></svg>1 keer per maand</li>
        <li><svg width="9" height="9" viewBox="0 0 10 10"><circle cx="5" cy="5" r="5" fill="#123e84"/><path d="M2.8 5.1l1.5 1.5 2.9-3" stroke="#fff" stroke-width="1.3" fill="none"/></svg>Exclusieve tips en promo’s</li>
        <li><svg width="9" height="9" viewBox="0 0 10 10"><circle cx="5" cy="5" r="5" fill="#123e84"/><path d="M2.8 5.1l1.5 1.5 2.9-3" stroke="#fff" stroke-width="1.3" fill="none"/></svg>Al 4.251 abonnees</li>
        <li><svg width="9" height="9" viewBox="0 0 10 10"><circle cx="5" cy="5" r="5" fill="#123e84"/><path d="M2.8 5.1l1.5 1.5 2.9-3" stroke="#fff" stroke-width="1.3" fill="none"/></svg>1 keer per maand</li>
        <li><svg width="9" height="9" viewBox="0 0 10 10"><circle cx="5" cy="5" r="5" fill="#123e84"/><path d="M2.8 5.1l1.5 1.5 2.9-3" stroke="#fff" stroke-width="1.3" fill="none"/></svg>Exclusieve tips en promo’s</li>
      </ul>
    </div>
  </section>

  <footer class="site-footer">
    <div class="footer-col" style="left:140px">
      <h3>Contact us</h3>
      <p>Email: info@forgewell.example</p>
      <p>Phone: 0240555010</p>
    </div>
    <div class="footer-col" style="left:357px">
      <h3>Our slaes department</h3>
      <p>Street: xxx</p>
      <p>xxx City</p>
      <span class="map-button">View Map <svg width="15" height="10" viewBox="0 0 15 10"><path d="M1 1l4 4-4 4M7 1l4 4-4 4" stroke="#fff" stroke-width="2" fill="none"/></svg></span>
    </div>
    <div class="footer-col" style="left:614px">
      <h3>R&amp;D and production</h3>
      <p>Street: xxx</p>
      <p>xxx City2</p>
      <span class="map-button">View Map <svg width="15" height="10" viewBox="0 0 15 10"><path d="M1 1l4 4-4 4M7 1l4 4-4 4" stroke="#fff" stroke-width="2" fill="none"/></svg></span>
    </div>
    <div class="footer-bottom">Copyright © 2015 forgewell.example. All rights reserved</div>
  </footer>
</div>
</body>
</html>
```